Business Card

We need some ideas for corporate business cards. I'm interested in a double sided card, with one side featuring our corporate logo, the other side with employee information.

Corporate colors, logo etc. available at www.brivalo.com

Industry/Entity Type

Business

Requirements
Must have
• The "Brivalo" logo with stylized "O"

Nice to have
• Preferred font is calibri

```html
<!DOCTYPE html>
<html lang="en">
<head>
<meta charset="utf-8">
<title>Brivalo Business Card</title>
<link rel="stylesheet" href="https://fonts.googleapis.com/css2?family=Exo+2:wght@400;500;600&display=swap">
<style>
  :root {
    --stage: #b9bbbf;
    --brand-blue: #4a63a3;
    --brand-blue-light: #8d9cc6;
    --ink: #1d1f24;
    --card-white: #f7f7f8;
    --card-grey: #e6e7e9;
    --motif-grey: #dcdde0;
  }
  * { margin: 0; padding: 0; box-sizing: border-box; }
  html, body {
    width: 1200px;
    height: 900px;
    overflow: hidden;
    background: var(--stage);
    font-family: "Exo 2", "Segoe UI", sans-serif;
  }
  .stage {
    position: relative;
    width: 1200px;
    height: 900px;
  }
  .card {
    position: absolute;
    top: 290px;
    width: 510px;
    height: 320px;
    border-radius: 16px;
    overflow: hidden;
    box-shadow: 0 6px 18px rgba(0,0,0,0.18);
  }

  /* Back side */
  .card-back {
    left: 70px;
    background: var(--brand-blue);
  }
  .card-back .pattern {
    position: absolute;
    inset: 0;
    background: linear-gradient(135deg, var(--brand-blue-light) 0%, var(--brand-blue) 55%, var(--brand-blue-light) 100%);
  }
  .card-back .logo-strip {
    position: absolute;
    left: 230px;
    right: 0;
    top: 178px;
    height: 74px;
    background: var(--brand-blue);
    display: flex;
    align-items: center;
    padding-left: 22px;
  }
  .card-back .wordmark {
    font-weight: 500;
    font-size: 50px;
    letter-spacing: 4px;
    color: var(--ink);
    line-height: 1;
  }

  /* Front side */
  .card-front {
    left: 620px;
    background: linear-gradient(160deg, var(--card-white) 0%, var(--card-grey) 100%);
  }
  .card-front .motif {
    position: absolute;
    left: 170px;
    top: 60px;
    width: 320px;
    height: 210px;
    background: linear-gradient(120deg, rgba(220,221,224,0) 0%, var(--motif-grey) 60%, rgba(220,221,224,0.4) 100%);
  }
  .card-front .brand {
    position: absolute;
    left: 36px;
    top: 108px;
    display: flex;
    align-items: center;
    gap: 10px;
  }
  .card-front .brand-mark {
    width: 22px;
    height: 22px;
    background: var(--brand-blue);
  }
  .card-front .wordmark {
    font-weight: 500;
    font-size: 38px;
    letter-spacing: 3px;
    color: var(--brand-blue);
    line-height: 1;
  }
  .person {
    position: absolute;
    left: 300px;
    top: 30px;
  }
  .person-name {
    font-size: 17px;
    font-weight: 500;
    color: var(--ink);
    letter-spacing: 0.5px;
  }
  .person-role {
    font-size: 13px;
    color: var(--brand-blue);
  }
  .contact {
    position: absolute;
    left: 318px;
    top: 118px;
    list-style: none;
    font-size: 14px;
    line-height: 20px;
    color: var(--ink);
  }
  .contact .label, .contact .accent { color: var(--brand-blue); }
  .address {
    position: absolute;
    left: 36px;
    top: 196px;
    font-style: normal;
    font-size: 14px;
    line-height: 18px;
    color: var(--ink);
  }
  .card-front .band {
    position: absolute;
    left: 0;
    right: 0;
    bottom: 0;
    height: 18px;
    background: var(--brand-blue);
  }
</style>
</head>
<body>
<main class="stage">
  <section class="card card-back" aria-label="Card back">
    <div class="pattern" role="img" aria-label="Repeating white brand-symbol pattern on blue"></div>
    <div class="logo-strip">
      <span class="wordmark">BRIVALO</span>
    </div>
  </section>

  <section class="card card-front" aria-label="Card front">
    <div class="motif" role="img" aria-label="Faint grey arrow motif"></div>
    <div class="brand">
      <span class="brand-mark"></span>
      <span class="wordmark">BRIVALO</span>
    </div>
    <div class="person">
      <p class="person-name">DANIEL MORAN</p>
      <p class="person-role">Lead Manager</p>
    </div>
    <ul class="contact">
      <li><span class="label">Tel:</span> +353 1 555 0142</li>
      <li><span class="label">Fax:</span> +353 1 555 0199</li>
      <li><span class="accent">info@</span>brivalo.com</li>
      <li>www.<span class="accent">brivalo</span>.com</li>
    </ul>
    <address class="address">
      14 Alder Row,<br>
      Greenfield Business Park, Dublin 12<br>
      Dublin, DB<br>
      Ireland
    </address>
    <div class="band"></div>
  </section>
</main>
</body>
</html>
```